Political sign design, fonts colors and layout

I am running for Town Council.

My message is done, and *a draft is attached* with the text we wish to use. It says "Elect Dana Velloway" etc. In Maroon and White. I am not a designer, but this is somewhat close to what we are looking for.

I need help with colors and fonts, layout, spacing, and general cleanup.

I'm attaching the town high school logo:

- "B" for Brockmere: with black and white outlines on the fonts
- we want to incorporate the black and white on the fonts
- for the entire text, parts of the text, or best would be a mix

This is for signs printed and placed all over my town.

We need two versions

1. square, 4' by 4' version
2. 36" by 24" version

The smaller version will drop the three bullet pointed text, but otherwise can be identical.

The sign can only use 3 printed colors (due to printing costs.)

1. maroon,
2. white,
3. black.

The maroon should match the maroon from the high school logo attached, which I believe I did in the draft.

We also like the white border around the outside, like in the "scoreboard" design attached.

Thanks for your attention, wish me luck.

Dana

Target Market(s)

SIgns, Political market

Industry/Entity Type

Political

Font styles to use
Sans Serif
Other font styles liked:
• Arial Black, Sans Serif Bold

Requirements
Must have
• maroon background, white font.
• - black borders around fonts where appropriate
• - great spacing
• - great typeface usage
• - clean and crisp political sign, visible while driving.
• - my name "Dana Velloway" much larger like the draft, or the appropriate additional size
• - two versions, one square, and one 36" / 24"
Nice to have
• - nice borders
• - dress it up a bit, using italics and bold fonts, without making it flashy or busy.
Should not have
• Must be easily readable from a car, except for "Paid for by Friends of Dana Velloway" which can be tiny.
• Colors are noted in the description, the "Brockmere Maroon" as the background, white font, and some use of black.

```html
<!DOCTYPE html>
<html lang="en">
<head>
<meta charset="utf-8">
<title>Elect Dana Velloway – Yard Signs</title>
<link href="https://fonts.googleapis.com/css2?family=Anton&family=Archivo+Black&family=Archivo:ital,wght@1,800&family=Inter:wght@300&family=Roboto+Condensed:wght@400&display=swap" rel="stylesheet">
<style>
  :root {
    --maroon: #74112f;
    --white: #ffffff;
    --ink: #231f20;
    --star: #000000;
    --backdrop: #d1d2d4;
  }
  html, body { margin: 0; padding: 0; overflow: hidden; background: var(--backdrop); }
  .sheet { display: block; width: 1074px; height: 1200px; }
  .backdrop { fill: var(--backdrop); }
  .field { fill: var(--maroon); }
  .frame { fill: none; stroke: var(--white); }
  .rule { stroke: var(--white); }
  .ballot-band { fill: var(--ink); }
  .kicker { font-family: "Archivo Black", "Arial Black", sans-serif; fill: var(--white); }
  .kicker .star { fill: var(--star); }
  .slogan { font-family: "Inter", Helvetica, Arial, sans-serif; font-weight: 300; fill: var(--white); letter-spacing: -0.02em; }
  .issue { font-family: "Roboto Condensed", "Arial Narrow", sans-serif; fill: var(--white); }
  .issue-box { fill: none; stroke: var(--white); stroke-width: 3.5; }
  .issue-tick { fill: none; stroke: var(--white); stroke-width: 4; stroke-linecap: round; stroke-linejoin: round; }
  .elect, .office { font-family: "Archivo", Arial, sans-serif; font-style: italic; font-weight: 800; fill: var(--white); }
  .first-name, .last-name {
    font-family: "Archivo Black", "Arial Black", sans-serif;
    fill: var(--white); stroke: var(--ink); stroke-linejoin: round; paint-order: stroke;
  }
  .web { font-family: "Archivo Black", "Arial Black", sans-serif; fill: var(--white); letter-spacing: 0.04em; }
  .vote-date {
    font-family: "Anton", Impact, sans-serif; fill: var(--maroon);
    stroke: var(--white); stroke-linejoin: round; paint-order: stroke;
  }
  .disclaimer { font-family: "Archivo", Arial, sans-serif; font-style: italic; fill: var(--white); font-weight: 400; }
</style>
</head>
<body>
<svg class="sheet" viewBox="0 0 1342 1500" xmlns="http://www.w3.org/2000/svg" role="img" aria-label="Elect Dana Velloway yard signs, square and landscape versions">
  <rect class="backdrop" x="0" y="0" width="1342" height="1500"/>

  <!-- Square sign -->
  <g class="sign sign--square">
    <rect class="field" x="444" y="82" width="454" height="454"/>
    <rect class="frame" x="455" y="93" width="432" height="432" stroke-width="5"/>
    <text class="kicker" x="671" y="132" font-size="19" text-anchor="middle" textLength="356" lengthAdjust="spacingAndGlyphs"><tspan class="star">★★★</tspan> Fighting for Brockmere <tspan class="star">★★★</tspan></text>
    <text class="slogan" x="671" y="173" font-size="38" text-anchor="middle" textLength="354" lengthAdjust="spacingAndGlyphs">Take back our Town!</text>
    <text class="elect" x="475" y="210" font-size="19">Elect</text>
    <line class="rule" x1="530" y1="203" x2="866" y2="203" stroke-width="3"/>
    <text class="first-name" x="480" y="278" font-size="80" stroke-width="8" textLength="382" lengthAdjust="spacing">DANA</text>
    <text class="last-name" x="480" y="378" font-size="118" stroke-width="9" textLength="382" lengthAdjust="spacingAndGlyphs">VELLOWAY</text>
    <line class="rule" x1="476" y1="398" x2="538" y2="398" stroke-width="3"/>
    <text class="office" x="865" y="404" font-size="17" text-anchor="end">for Brockmere Councilman / Trustee</text>
    <text class="web" x="671" y="436" font-size="18" text-anchor="middle">www.votedana.com</text>
    <rect class="ballot-band" x="458" y="450" width="426" height="47"/>
    <text class="vote-date" x="671" y="487" font-size="34" stroke-width="4" text-anchor="middle" textLength="289" lengthAdjust="spacingAndGlyphs">Vote Nov. 8<tspan font-size="20" dy="-12">th</tspan><tspan dy="12"> Row A</tspan></text>
    <text class="disclaimer" x="876" y="513" font-size="9" text-anchor="end">paid for by friends of Dana Velloway</text>
  </g>

  <!-- Landscape sign -->
  <g class="sign sign--landscape">
    <rect class="field" x="0" y="612" width="1342" height="888"/>
    <rect class="frame" x="23" y="635" width="1296" height="842" stroke-width="14"/>
    <text class="kicker" x="86" y="712" font-size="36" textLength="682" lengthAdjust="spacingAndGlyphs"><tspan class="star" font-size="40">★★★</tspan> Fighting for Brockmere <tspan class="star" font-size="40">★★★</tspan></text>
    <text class="slogan" x="84" y="792" font-size="80" textLength="680" lengthAdjust="spacingAndGlyphs">Take back our Town!</text>

    <g class="issues">
      <g transform="translate(808 684)">
        <rect class="issue-box" x="0" y="2" width="24" height="24" rx="4"/>
        <path class="issue-tick" d="M6 13 L12 19 L28 1"/>
      </g>
      <text class="issue" x="846" y="711" font-size="37">Stop HIGH taxes</text>
      <g transform="translate(808 725)">
        <rect class="issue-box" x="0" y="2" width="24" height="24" rx="4"/>
        <path class="issue-tick" d="M6 13 L12 19 L28 1"/>
      </g>
      <text class="issue" x="846" y="752" font-size="37">Clean up our government</text>
      <g transform="translate(808 767)">
        <rect class="issue-box" x="0" y="2" width="24" height="24" rx="4"/>
        <path class="issue-tick" d="M6 13 L12 19 L28 1"/>
      </g>
      <text class="issue" x="846" y="794" font-size="37" textLength="420" lengthAdjust="spacingAndGlyphs">Preserve our neighborhoods</text>
    </g>

    <text class="elect" x="86" y="870" font-size="37">Elect</text>
    <line class="rule" x1="194" y1="856" x2="1264" y2="856" stroke-width="6"/>
    <text class="first-name" x="96" y="1022" font-size="188" stroke-width="22" textLength="1162" lengthAdjust="spacing">DANA</text>
    <text class="last-name" x="96" y="1255" font-size="290" stroke-width="24" textLength="1164" lengthAdjust="spacingAndGlyphs">VELLOWAY</text>
    <line class="rule" x1="86" y1="1288" x2="618" y2="1288" stroke-width="6"/>
    <text class="office" x="1263" y="1300" font-size="34" text-anchor="end">for Brockmere Councilman / Trustee</text>

    <rect class="ballot-band" x="30" y="1345" width="1282" height="90"/>
    <text class="web" x="152" y="1404" font-size="38">www.votedana.com</text>
    <text class="vote-date" x="628" y="1415" font-size="66" stroke-width="8" textLength="567" lengthAdjust="spacingAndGlyphs">Vote Nov. 8<tspan font-size="38" dy="-24">th</tspan><tspan dy="24"> Row A</tspan></text>
    <text class="disclaimer" x="1296" y="1459" font-size="18" text-anchor="end">paid for by friends of Dana Velloway</text>
  </g>
</svg>
</body>
</html>
```